Pivora has a great new logo - now we need a website!!

Pivora has been in business for a long time and needs to start a new era. Additional to other changes being made in the business itself, Pivora needs an overhaul of its entire branding. PART 1 is COMPLETE - we have our new logo!

Next step... new website! That's where you come in.

Pivora provides a range of computer related services including computer maintenance, networking, sales & cloud services. We provide onsite (field) and remote support. Our customers range from homes to companies with 100+ computers. We pride ourselves on clear and honest communication.

We are a small business but want a professional yet easy-going look that shows the 'cool' side of having your computer system cared for. The website should exude trustworthiness and professionalism but still get comments like 'modern' and 'smart design'. We want our customers to feel that choosing any other company to maintain their system would be a 'geeky' choice.

We like clear thinking so an uncluttered, well organised structure is appreciated. Obvious references to calling or emailing us would be good so people dont need to search around for our contact details.

We look after both Quince & Veltharon operating systems so there needs to be universal appeal rather than a look associated with only one of these two brands.

We want to wow our current clients but also attract new ones so a focus on SEO is a must. And a focus on social media too with links/feeds to Chatterly, chirpex and WorkLoop!

Have a look at www.pivora.com.au so you can see for yourself how much you can help us!

**Breathe new life into Pivora's online presence!**

(We do have a separate website www.kelbrohome.com.au that we set as the homepage for our clients - we like how it is but it might need freshening up to match our new site. We will also want our chatterly page totally made over. You'll probably have other suggestions of things we should be doing. We want to form an ongoing relationship with the right designer!)

(Also, we are open to suggestions regarding the logo size and colour)
Updates

I dont want to cramp anyones creativity but i like this: http://www.quindlework.com/demo/themes/wordpress/2011/saffron/

I'm obivously happy to see your own ideas too!

I also like this one: http://marbleloft.net/item/dralo-responsive-wordpress-theme/7184206

Clarification: We are looking for a working, implemented website, not just design of the theme. Once the general page layout is done we can do the majority of the content input. But we do want a workable shell with images.

We are open to buying existing themes if that helps. Thanks!

Site also needs email contact form, testimonial submission page, blog (feed to home page), chatterly like button

Reason: I haven't found the ideal one yet... We want some other designers to send their ideas.

Reason: We need a little more time to make our decision.

Target Market(s)

Mainly small to medium businesses but also homes

Industry/Entity Type

Small Business

Requirements
Must have
• SEO
Social Media
That little address bar icon
R in a circle at the bottom of the site to show we have trademarked our company name
A finished product website with content and images that we can modify ourselves over time.

```html
<!DOCTYPE html>
<html lang="en">
<head>
<meta charset="utf-8">
<title>Pivora – IT Solutions &amp; Support</title>
<link rel="stylesheet" href="https://fonts.googleapis.com/css2?family=Oswald:wght@300;400&family=Ubuntu:wght@400;500&display=swap">
<style>
:root{
  --brand-blue:#5a6b9e;
  --brand-blue-dark:#3f4f80;
  --ink:#2f2b2a;
  --text:#3b3b3b;
  --muted:#9a9a9a;
  --panel:#ededed;
  --hero:#efefef;
  --dark:#333232;
  --dark-box:#3b3431;
  --white:#ffffff;
}
*{box-sizing:border-box;margin:0;padding:0}
html,body{width:1000px;height:1200px;overflow:hidden;background:var(--white)}
body{position:relative;font-family:"Ubuntu",sans-serif;color:var(--text)}
.abs{position:absolute}
.display{font-family:"Oswald",sans-serif;font-weight:400;text-transform:uppercase}

.top-strip{left:0;top:0;width:1000px;height:10px;background:var(--brand-blue)}

.logo{left:74px;top:34px;display:flex;align-items:center;gap:12px}
.logo-mark{width:56px;height:56px;border-radius:50%;background:var(--brand-blue)}
.logo-name{font-family:"Ubuntu",sans-serif;font-weight:500;font-size:30px;color:var(--ink);line-height:1}
.logo-tag{font-size:13px;color:#666;margin-top:3px}

.search{left:783px;top:31px;width:142px;height:23px;border:1px solid #d6d6d6;border-radius:2px;font-size:9.5px;font-style:italic;color:#aaa;padding:5px 10px;display:flex;justify-content:space-between}

.main-nav{left:375px;top:71px;width:550px;height:34px;border-radius:17px;background:linear-gradient(#6a7bb0,var(--brand-blue-dark));display:flex;overflow:hidden;box-shadow:0 2px 2px rgba(0,0,0,.15)}
.main-nav a{color:#fff;text-decoration:none;font-size:11.5px;display:flex;align-items:center;justify-content:center;border-left:1px solid rgba(255,255,255,.18);padding:0 18px}
.main-nav a.home{width:54px;background:var(--brand-blue-dark);border:none}

.hero{left:0;top:136px;width:1000px;height:275px;background:var(--hero);border-top:1px solid #e2e2e2}
.hero-title{left:92px;top:60px;font-size:26px;color:var(--brand-blue);font-weight:300;letter-spacing:-.3px}
.hero-sub{left:92px;top:96px;font-size:26px;color:var(--ink);font-weight:300}
.hero-btn{left:92px;top:140px;width:86px;height:29px;background:var(--ink);color:#fff;font-size:14px;font-weight:300;display:flex;align-items:center;justify-content:center;border-radius:2px}
.hero-dots{left:95px;top:246px;display:flex;gap:14px}
.hero-dots span{width:10px;height:10px;border-radius:50%;background:#6b6b6b}
.hero-dots span:first-child{background:var(--brand-blue)}
.hero-photo{left:425px;top:0;width:485px;height:275px;background:linear-gradient(90deg,var(--hero),#dfe3ea 25%,#cfd3da 60%,#e9ebee)}

.feature{top:440px;width:257px}
.feature-head{display:flex;align-items:center;gap:12px;height:42px;padding-bottom:0}
.feature-icon{width:38px;height:38px}
.feature-head h2{font-size:27px;color:var(--ink)}
.feature-rule{height:1px;background:#dcdcdc;margin:18px 0 12px}
.feature p{font-size:11px;line-height:19.2px;text-align:justify;color:var(--text)}
.feature-btn{margin-top:9px;height:29px;background:#e8e8e8;display:flex;align-items:center;justify-content:flex-end;padding-right:12px;font-family:"Oswald",sans-serif;font-size:13px;color:var(--ink);text-transform:uppercase}

.what{left:74px;top:705px;width:553px}
.what h2{font-size:23px;color:var(--brand-blue);font-weight:400;margin-bottom:10px}
.what p{font-size:10.8px;line-height:19px;margin-bottom:5px}
.callout{left:73px;top:840px;width:554px;height:71px;background:var(--brand-blue);border-radius:6px;color:#fff;display:flex;align-items:center;justify-content:center;gap:14px}
.callout-text{text-align:center;font-size:20px;line-height:27px;font-weight:400}

.service-list{left:668px;top:708px;width:257px;height:203px;background:linear-gradient(#4a423e,var(--dark-box));border:2px solid #2a2523;padding:18px 0 0 16px;display:grid;grid-template-columns:118px 120px;row-gap:11.5px;align-content:start}
.service-list li{list-style:none;font-size:10.3px;color:#eee}
.service-list li::before{content:"››";margin-right:8px;color:#ccc}

.contact-strip{left:0;top:940px;width:1000px;height:73px;background:radial-gradient(ellipse at center,#fafafa 30%,#f1f1f1 100%)}
.contact-item{top:20px;display:flex;align-items:center;gap:10px;font-family:"Oswald",sans-serif;font-weight:300;font-size:27px;color:var(--ink)}
.contact-divider{left:487px;top:18px;width:1px;height:38px;background:#d8d8d8}

.footer{left:0;top:1013px;width:1000px;height:187px;background:var(--dark);color:#fff}
.foot-col{top:16px}
.foot-col h3{font-weight:400;font-size:12.5px;color:#fff;padding-bottom:13px;border-bottom:1px solid #4a4a4a;width:242px}
.foot-col h4{font-weight:400;font-size:10.8px;margin:13px 0 8px}
.foot-col p{font-size:9.8px;line-height:15.5px;color:#9d9d9d}
.foot-col .date{color:#8ea0d6}
.newsletter-field{width:241px;height:33px;margin-top:10px;background:#f0f0f0;border:2px solid #cfcfcf;display:flex;align-items:center;justify-content:space-between;padding:0 4px 0 10px;font-size:10px;color:#333}
.newsletter-field span.btn{background:linear-gradient(#bdbdbd,#8b8b8b);color:#333;font-family:Georgia,serif;font-weight:bold;font-size:9.5px;padding:3px 9px;border-radius:3px}
.foot-rule{left:74px;top:1153px;width:851px;height:1px;background:#474747}
.copyright{left:74px;top:1171px;font-size:10px;color:#ccc}
.social{left:849px;top:1168px;display:flex;gap:9px}
.social span{width:19px;height:19px;background:#6f6f6f;border-radius:2px}
</style>
</head>
<body>
<div class="abs top-strip"></div>

<header>
  <div class="abs logo">
    <div class="logo-mark"></div>
    <div>
      <div class="logo-name">Pivora</div>
      <div class="logo-tag">IT Solutions &amp; Support</div>
    </div>
  </div>
  <div class="abs search"><span>Search</span>
    <svg width="10" height="10" viewBox="0 0 10 10"><circle cx="4" cy="4" r="3" fill="none" stroke="#bbb" stroke-width="1.2"/><line x1="6.2" y1="6.2" x2="9" y2="9" stroke="#bbb" stroke-width="1.4"/></svg>
  </div>
  <nav class="abs main-nav">
    <a class="home" href="#" aria-label="Home"><svg width="14" height="13" viewBox="0 0 14 13"><path d="M7 0L0 6h2v7h4V9h2v4h4V6h2z" fill="#fff"/></svg></a>
    <a href="#">Services</a><a href="#">Pricing</a><a href="#">Opening Hours</a><a href="#">Pay Bill</a><a href="#">Links</a><a href="#" style="border-left:1px solid rgba(255,255,255,.18)">Contact us</a>
  </nav>
</header>

<section class="abs hero">
  <div class="abs hero-photo" role="img" aria-label="Photo of a confident business team looking upward"></div>
  <div class="abs display hero-title">Pellentesque vulputate auctor</div>
  <div class="abs display hero-sub">Suspendisse mollis</div>
  <div class="abs display hero-btn">View more</div>
  <div class="abs hero-dots"><span></span><span></span><span></span><span></span></div>
</section>

<section class="abs feature" style="left:74px">
  <div class="feature-head">
    <svg class="feature-icon" viewBox="0 0 38 38"><circle cx="19" cy="19" r="17" fill="none" stroke="#3a3532" stroke-width="3"/><path d="M10 12c4-2 7 0 8 3s-3 4-2 8 4 5 2 8c-6-1-10-7-8-19zM22 8c4 1 8 5 8 10-3 0-5-2-7-1s-2-5-1-9z" fill="#3a3532"/></svg>
    <h2 class="display">Support</h2>
  </div>
  <div class="feature-rule"></div>
  <p>Sed ut perspiciatis unde omnis iste natus error sit voluptatem doloremque laudantium, totam rem ape riam, eaque ipsa quae ab illo vitae dicta sunt explicabo. Nemo enim ipsam voluptatem quia voluptas sit asper natur aut odit aut fugit, sed quia consequuntur magni dolores eos qui ratione voluptatem.</p>
  <div class="feature-btn">View more</div>
</section>

<section class="abs feature" style="left:371px">
  <div class="feature-head">
    <svg class="feature-icon" viewBox="0 0 38 38"><circle cx="19" cy="19" r="17" fill="none" stroke="#3a3532" stroke-width="3"/><circle cx="19" cy="19" r="12" fill="#3a3532"/><text x="19" y="25" text-anchor="middle" font-family="Ubuntu,sans-serif" font-size="17" font-weight="500" fill="#fff">$</text></svg>
    <h2 class="display">Sales</h2>
  </div>
  <div class="feature-rule"></div>
  <p>Sed ut perspiciatis unde omnis iste natus error sit voluptatem doloremque laudantium, totam rem ape riam, eaque ipsa quae ab illo vitae dicta sunt explicabo. Nemo enim ipsam voluptatem quia voluptas sit asper natur aut odit aut fugit, sed quia consequuntur magni dolores eos qui ratione voluptatem.</p>
  <div class="feature-btn">View more</div>
</section>

<section class="abs feature" style="left:668px">
  <div class="feature-head">
    <svg class="feature-icon" viewBox="0 0 38 38"><circle cx="27" cy="10" r="8" fill="none" stroke="#3a3532" stroke-width="1.6"/><line x1="19" y1="10" x2="35" y2="10" stroke="#3a3532" stroke-width="1.2"/><line x1="27" y1="2" x2="27" y2="18" stroke="#3a3532" stroke-width="1.2"/><path d="M4 36l4-14-4 2 7-10 3 11-3-2-2 13zM14 34l8-12-3 0 10-6-2 11-2-3-7 12z" fill="#3a3532"/></svg>
    <h2 class="display">Internet services</h2>
  </div>
  <div class="feature-rule"></div>
  <p>Sed ut perspiciatis unde omnis iste natus error sit voluptatem doloremque laudantium, totam rem ape riam, eaque ipsa quae ab illo vitae dicta sunt explicabo. Nemo enim ipsam voluptatem quia voluptas sit asper natur aut odit aut fugit, sed quia consequuntur magni dolores eos qui ratione voluptatem.</p>
  <div class="feature-btn">View more</div>
</section>

<section class="abs what">
  <h2 class="display">What we do</h2>
  <p>Many IT problems are solved by restarting a computer. When this doesn't fix it, PIVORA will.</p>
  <p>At Pivora, we provide a range of computer related services. From new computers to website design &amp; hosting, we can help you with almost any technological need. We specialise in onsite computer installation and network setups. In the home or office, when you need computer assistance, call Pivora.</p>
</section>

<div class="abs callout">
  <svg width="34" height="38" viewBox="0 0 34 38"><path d="M6 2c3-1 5 0 6 3l2 6c0 2-2 3-3 4 1 4 4 8 8 11 1-1 2-3 4-3l6 3c2 1 3 3 2 6-1 3-4 5-7 4C12 33 3 20 2 9 2 6 3 3 6 2z" fill="#fff"/></svg>
  <div class="display callout-text">"One call to Pivora could help solve it all."<br>Simply call (03) 90417300</div>
</div>

<ul class="abs service-list">
  <li>Troubleshooting</li><li>Internet Connections</li>
  <li>Computer Sales</li><li>Website Hosting</li>
  <li>Networking</li><li>Exchange Email</li>
  <li>Hardware Repairs</li><li>Remote Access</li>
  <li>Virus Removal</li><li></li>
  <li>Offsite Backup</li>
</ul>

<section class="abs contact-strip">
  <div class="abs contact-item" style="left:166px">
    <svg width="28" height="28" viewBox="0 0 28 28"><path d="M4 18v-4a10 10 0 0 1 20 0v4" fill="none" stroke="#444" stroke-width="2.5"/><rect x="2" y="16" width="6" height="10" rx="2" fill="#555"/><rect x="20" y="16" width="6" height="10" rx="2" fill="#555"/></svg>
    <span>Hotline&nbsp; - &nbsp;(03)&nbsp; 9041 7300</span>
  </div>
  <div class="abs contact-divider"></div>
  <div class="abs contact-item" style="left:538px">
    <svg width="38" height="26" viewBox="0 0 38 26"><rect x="1" y="1" width="36" height="24" fill="#f4f4f4" stroke="#bbb"/><path d="M1 1l18 13L37 1" fill="none" stroke="#bbb"/></svg>
    <span>E- Mail&nbsp; - &nbsp;info@pivora.com</span>
  </div>
</section>

<footer class="abs footer">
  <div class="abs foot-col" style="left:75px">
    <h3>Latest news</h3>
    <h4>Excepteur sint occaecat cupidatat</h4>
    <p>Lorem ipsum dolor sit amet, consectetuer a iscing elit.<br>Aenean commodo ligula eget dolo.<br><span class="date">September 4th, 2010</span></p>
  </div>
  <div class="abs foot-col" style="left:386px">
    <h3>Latest Blog</h3>
    <h4>Excepteur sint occaecat cupidatat</h4>
    <p>Lorem ipsum dolor sit amet, consectetuer a iscing elit.<br>Aenean commodo ligula eget dolo.<br><span class="date">September 4th, 2010</span></p>
  </div>
  <div class="abs foot-col" style="left:683px">
    <h3 style="border:none;padding-bottom:0">Subscribe for Newsletter</h3>
    <div class="newsletter-field"><span>Your email address...</span><span class="btn">SUBMIT</span></div>
    <p style="color:#ccc;margin-top:14px">Lorem ipsum dolor sit amet, consectetuer a iscing elit.<br>Aenean commodo ligula eget dolo.</p>
  </div>
</footer>
<div class="abs foot-rule"></div>
<div class="abs copyright">Copyright © 2012 www.pivora.com.au &nbsp;&nbsp;&nbsp;All rights reserved.</div>
<div class="abs social"><span aria-label="Chatterly"></span><span aria-label="chirpex"></span><span aria-label="WorkLoop"></span></div>
</body>
</html>
```